International Travel Technology R&D business needs a wordpress website

We are a start up team of initially 2 individuals but plan to grow our team quickly, we have deep experience in travel technology. Our goal is to provide next generation technology research and development on behalf of our clients who are leading players in the travel technology industry. Attached our logos.

Target Market(s)

Travel Technology companies

Industry/Entity Type

Travel Industry

Coding

Coded - Design and coding required

Font styles to use
Sans Serif

Requirements
Must have
• Make use of our logo and colour scheme in the attached. Has to have a sense of adventure/ stepping into the unknown but equally must convey a sense of professionalism , we are a safe pair of hands. Sample themes are in the attachment .
Nice to have
• We have identified a theme on layoutgrove which we feel would be inspirational. We hahe attached them to help in the design as inspiration.
Should not have
• images of airplanes , hotels etc, we want to project a future image.

```html
<!DOCTYPE html>
<html lang="en">
<head>
<meta charset="utf-8">
<title>Skyward Path Labs</title>
<link href="https://fonts.googleapis.com/css2?family=Roboto:wght@300;400;500;700&family=Nothing+You+Could+Do&display=swap" rel="stylesheet">
<style>
  :root{
    --blue:#3aa3e3;
    --blue-dark:#1e6fb0;
    --navy:#1f3c73;
    --green:#5cb531;
    --ink:#2b2b2b;
    --muted:#555b61;
    --pale:#f3f5f7;
    --white:#ffffff;
  }
  *{box-sizing:border-box;margin:0;padding:0}
  html,body{width:1200px;height:2264px;overflow:hidden}
  body{position:relative;background:var(--white);font-family:'Roboto',Arial,sans-serif;color:var(--ink)}
  .abs{position:absolute}

  /* top bar */
  .topbar{left:0;top:0;width:1200px;height:33px;background:var(--white)}
  .topbar-items{right:58px;top:6px;display:flex;align-items:center;gap:26px;font-size:14px;color:var(--green)}
  .topbar-item{display:flex;align-items:center;gap:6px}
  .login{background:var(--green);color:var(--white);border-radius:3px;padding:2px 8px;font-size:14px;display:flex;gap:5px;align-items:center}
  .dot-social{width:11px;height:11px;border-radius:50%;background:var(--green)}

  .nav{left:0;top:33px;width:1200px;height:67px;background:var(--blue)}
  .nav-menu{right:52px;top:58px;display:flex;gap:34px;color:var(--white);font-weight:500;font-size:16px;letter-spacing:.2px}

  .brand{left:54px;top:0;width:284px;height:115px;background:var(--white);border-radius:0 0 12px 12px;box-shadow:0 2px 6px rgba(0,0,0,.12);display:flex;align-items:center;justify-content:center;gap:10px}
  .brand-mark{width:22px;height:22px;border-radius:50%;background:var(--blue)}
  .brand-name{font-family:'Roboto',Arial,sans-serif;font-weight:700;font-size:25px;color:var(--navy)}

  /* hero */
  .hero{left:0;top:100px;width:1200px;height:488px;background:linear-gradient(160deg,#6f8497 0%,#a8b6c3 40%,#cfd8e0 60%,#7e93a8 100%)}
  .hero-title{left:0;top:160px;width:1200px;text-align:center;font-family:'Nothing You Could Do',cursive;color:var(--white);font-size:74px;line-height:84px}
  .hero-sub{left:0;top:342px;width:1200px;text-align:center;color:var(--white);font-weight:500;font-size:21px;line-height:29px}
  .btn{top:425px;height:31px;font-size:10px;font-weight:700;display:flex;align-items:center;justify-content:center;border-radius:2px;letter-spacing:.3px}
  .btn-solid{left:495px;width:71px;background:var(--white);color:var(--navy)}
  .btn-ghost{left:616px;width:95px;border:1px solid var(--white);color:var(--white)}
  .hero-dots{left:566px;top:553px;display:flex;gap:9px}
  .hero-dots span{width:10px;height:10px;border-radius:50%;border:1px solid var(--white)}
  .hero-dots span.on{background:var(--white)}

  /* features */
  .features{left:0;top:588px;width:1200px;height:363px;background:var(--pale)}
  .section-title{left:0;width:1200px;text-align:center;font-weight:700;font-size:22px;color:var(--ink)}
  .rule{height:0;border-top:2px dotted var(--green)}
  .feature{width:350px;text-align:center;top:694px}
  .feature-icon{width:78px;height:78px;background:var(--blue);margin:0 auto;display:flex;align-items:center;justify-content:center;border-radius:2px}
  .feature-title{margin-top:18px;font-weight:500;font-size:19px}
  .feature-text{margin-top:14px;font-size:13px;line-height:20px;color:var(--muted)}

  .cityscape{left:0;top:951px;width:1200px;height:274px;background:linear-gradient(180deg,#3d5a86 0%,#23365a 55%,#42618d 100%);box-shadow:0 -4px 10px rgba(58,163,227,.5),0 4px 10px rgba(58,163,227,.5)}

  /* services */
  .illustration{left:53px;top:1328px;width:533px;height:400px;background:linear-gradient(180deg,#e4f3fd 0%,#bfe2f8 70%,#a9d8f6 100%)}
  .accordion{left:616px;top:1352px;width:531px}
  .acc-item{display:flex;gap:13px;align-items:flex-start;font-size:16px;font-weight:300;color:var(--ink);position:absolute;left:0}
  .acc-toggle{width:26px;height:26px;flex:none;background:#eef2f5;display:flex;align-items:center;justify-content:center;border-radius:2px}
  .acc-item.open .acc-toggle{background:var(--blue)}
  .acc-item.open .acc-label{color:var(--blue)}
  .acc-label{line-height:26px}
  .acc-body{position:absolute;left:36px;top:1385px;width:500px;font-size:13px;line-height:20px;color:var(--muted);font-weight:400}

  .skyline{left:0;top:1750px;width:1200px;height:69px;background:linear-gradient(180deg,rgba(58,163,227,0) 0%,rgba(58,163,227,.55) 60%,var(--blue) 100%)}

  /* footer */
  .footer{left:0;top:1819px;width:1200px;height:445px;background:var(--blue);color:var(--white)}
  .f-col{top:1860px;width:254px}
  .f-title{font-weight:700;font-size:18px;margin-bottom:16px}
  .f-text{font-size:13px;line-height:20px}
  .f-line{font-size:13px;margin-top:14px}
  .f-line b{font-weight:700}
  .f-social{display:flex;gap:13px;margin-top:18px}
  .f-social span{width:12px;height:12px;border-radius:50%;background:var(--white)}
  .field{width:251px;height:31px;background:var(--white);border-radius:3px;font-size:13px;color:#888;padding:0 12px;display:flex;align-items:center;margin-bottom:20px}
  .field.area{height:50px;align-items:flex-start;padding-top:8px;margin-bottom:18px}
  .send{width:134px;height:31px;background:var(--green);color:var(--white);font-weight:700;font-size:13px;display:flex;align-items:center;justify-content:center;border-radius:2px}
  .map{width:254px;height:209px;background:linear-gradient(135deg,#eee6d6 0%,#f5f1e8 50%,#d8e6c8 100%)}
  .f-divider{left:53px;top:2196px;width:1094px;height:1px;background:rgba(0,0,0,.25)}
  .copyright{left:0;top:2221px;width:1200px;text-align:center;font-size:13px;font-weight:500}
</style>
</head>
<body>

<div class="abs topbar"></div>
<div class="abs nav"></div>
<div class="abs topbar-items">
  <div class="topbar-item">
    <svg width="13" height="13" viewBox="0 0 24 24"><path fill="#5cb531" d="M6.6 10.8a15.1 15.1 0 0 0 6.6 6.6l2.2-2.2c.3-.3.7-.4 1-.2 1.1.4 2.3.6 3.6.6.6 0 1 .4 1 1V20c0 .6-.4 1-1 1A17 17 0 0 1 3 4c0-.6.4-1 1-1h3.5c.6 0 1 .4 1 1 0 1.3.2 2.5.6 3.6.1.3 0 .7-.2 1z"/></svg>
    <span>+1 800 555 01 47</span>
  </div>
  <div class="topbar-item">
    <svg width="14" height="11" viewBox="0 0 24 18"><rect x="0" y="0" width="24" height="18" rx="2" fill="#5cb531"/><path d="M1 1l11 9 11-9" stroke="#fff" stroke-width="2" fill="none"/></svg>
    <span>hello@skywardpath.example</span>
  </div>
  <div class="login">
    <svg width="11" height="11" viewBox="0 0 24 24"><path fill="#fff" d="M10 17l5-5-5-5v3H2v4h8zM14 3h6a2 2 0 0 1 2 2v14a2 2 0 0 1-2 2h-6v-2h6V5h-6z"/></svg>
    <span>Login</span>
  </div>
  <span class="dot-social"></span>
  <span class="dot-social"></span>
  <svg width="13" height="13" viewBox="0 0 24 24"><circle cx="10" cy="10" r="7" stroke="#5cb531" stroke-width="3" fill="none"/><path d="M15 15l7 7" stroke="#5cb531" stroke-width="3"/></svg>
</div>

<nav class="abs nav-menu">
  <span>HOME</span><span>COMPANY</span><span>SERVICES</span><span>SOLUTIONS</span><span>BLOG</span><span>CONTACT</span>
</nav>

<div class="abs brand">
  <span class="brand-mark"></span>
  <span class="brand-name">Skyward Path Labs</span>
</div>

<section>
  <div class="abs hero" role="img" aria-label="Blurred photograph of a business meeting table with printed bar charts and a glass"></div>
  <h1 class="abs hero-title">Welcome to<br>Skyward Path Labs</h1>
  <p class="abs hero-sub">Your trusted market research provider, dedicated to the<br>provision of meaningful and actionable insights</p>
  <a class="abs btn btn-solid">ABOUT US</a>
  <a class="abs btn btn-ghost">GO ON SURFING</a>
  <div class="abs hero-dots"><span class="on"></span><span></span><span class="on"></span><span class="on"></span></div>
</section>

<section>
  <div class="abs features"></div>
  <h2 class="abs section-title" style="top:613px">Partners &amp; Travel Technology Companies</h2>
  <div class="abs rule" style="left:41px;top:652px;width:1121px"></div>

  <div class="abs feature" style="left:50px">
    <div class="feature-icon">
      <svg width="40" height="40" viewBox="0 0 24 24" fill="none" stroke="#fff" stroke-width="1.5"><rect x="3" y="10" width="4" height="10"/><path d="M7 11l4-8c1.5 0 2 1 2 2l-1 4h6a2 2 0 0 1 2 2.3l-1.2 6.5A2 2 0 0 1 16.8 20H7"/></svg>
    </div>
    <h3 class="feature-title">Who we are</h3>
    <p class="feature-text">The quality perception of the product, what clients would like to change, what price can they afford, where is this product wanted the most, what causes dissatisfaction in a product (i.e. price, quality,design)</p>
  </div>
  <div class="abs feature" style="left:423px">
    <div class="feature-icon">
      <svg width="40" height="40" viewBox="0 0 24 24" fill="none" stroke="#fff" stroke-width="1.5"><path d="M12 2c3 3 4 7 3 12H9C8 9 9 5 12 2z"/><circle cx="12" cy="9" r="1.5"/><path d="M9 14l-2 3h3M15 14l2 3h-3M12 17v4"/></svg>
    </div>
    <h3 class="feature-title">Our Mission</h3>
    <p class="feature-text">Skyward Path Labs is a team of research professionals that work toward delivering research services while upholding the highest standards of design, analysis and reporting. Our mission is to help set the industry in consulting services</p>
  </div>
  <div class="abs feature" style="left:798px">
    <div class="feature-icon">
      <svg width="40" height="40" viewBox="0 0 24 24" fill="none" stroke="#fff" stroke-width="1.5"><path d="M5 2h10l4 4v16H5z"/><path d="M15 2v4h4M8 10h8M8 13h8M8 16h8"/></svg>
    </div>
    <h3 class="feature-title">Our Vision</h3>
    <p class="feature-text">Our vision is to be a long-term preferred partner to our clients in the field of market research and business consulting. We are relentlessly focused on delivering exceptional value in provision of strategy, research and analysis</p>
  </div>
</section>

<div class="abs cityscape" role="img" aria-label="Aerial photograph of a dense city skyline at dusk"></div>

<section>
  <h2 class="abs section-title" style="top:1253px">What We Do</h2>
  <div class="abs rule" style="left:54px;top:1293px;width:1093px"></div>
  <div class="abs illustration" role="img" aria-label="Flat blue illustration of three people working at laptops in front of city buildings and dashboard charts"></div>

  <div class="abs accordion">
    <div class="acc-item open" style="top:0">
      <span class="acc-toggle"><svg width="12" height="8" viewBox="0 0 12 8"><path d="M1 7l5-5 5 5" stroke="#fff" stroke-width="1.6" fill="none"/></svg></span>
      <span class="acc-label">Opinion Polling</span>
    </div>
    <p class="acc-body" style="top:34px">Opinion polls are an integral part of political debates, the state of the economy, social trends and more. Simply put, we report what people think, along with what they do, because it is important. We generate original public opinion data and other information that is relevant, timely and accurate</p>
    <div class="acc-item" style="top:134px"><span class="acc-toggle"><svg width="12" height="8" viewBox="0 0 12 8"><path d="M1 1l5 5 5-5" stroke="#3aa3e3" stroke-width="1.6" fill="none"/></svg></span><span class="acc-label">Social and Economic Policy Analysis</span></div>
    <div class="acc-item" style="top:190px"><span class="acc-toggle"><svg width="12" height="8" viewBox="0 0 12 8"><path d="M1 1l5 5 5-5" stroke="#3aa3e3" stroke-width="1.6" fill="none"/></svg></span><span class="acc-label">Project Evaluation and Impact Assessment</span></div>
    <div class="acc-item" style="top:247px"><span class="acc-toggle"><svg width="12" height="8" viewBox="0 0 12 8"><path d="M1 1l5 5 5-5" stroke="#3aa3e3" stroke-width="1.6" fill="none"/></svg></span><span class="acc-label">Feasibility Studies</span></div>
    <div class="acc-item" style="top:303px"><span class="acc-toggle"><svg width="12" height="8" viewBox="0 0 12 8"><path d="M1 1l5 5 5-5" stroke="#3aa3e3" stroke-width="1.6" fill="none"/></svg></span><span class="acc-label">New Product Development</span></div>
    <div class="acc-item" style="top:359px"><span class="acc-toggle"><svg width="12" height="8" viewBox="0 0 12 8"><path d="M1 1l5 5 5-5" stroke="#3aa3e3" stroke-width="1.6" fill="none"/></svg></span><span class="acc-label">Market Size and Segmentation Studies</span></div>
  </div>
</section>

<div class="abs skyline" role="img" aria-label="Blue silhouette of a city skyline and airport along the top of the footer"></div>

<footer>
  <div class="abs footer"></div>

  <div class="abs f-col" style="left:53px">
    <h4 class="f-title">Contact Us</h4>
    <p class="f-text">Maecenas etos sit amet, consectetur adipiscing elit. Terminal volutpat rutrum metro amet sollicitudin interdum.</p>
    <p class="f-line" style="margin-top:18px"><b>Phone:</b> +1 (800) 555 02 19</p>
    <p class="f-line"><b>Office:</b> 4410 Alder Lane, Fairhaven</p>
    <p class="f-line"><b>Email:</b> office@skywardpath.example</p>
    <div class="f-social"><span></span><span></span><span></span><span></span><span></span></div>
  </div>

  <div class="abs f-col" style="left:334px">
    <h4 class="f-title">Feel Free to Mail</h4>
    <div class="field">Name *</div>
    <div class="field">Email *</div>
    <div class="field area">Write Your Message Here...</div>
    <div class="send">SEND MESSAGE</div>
  </div>

  <div class="abs f-col" style="left:614px">
    <h4 class="f-title">Headquarters</h4>
    <div class="map" role="img" aria-label="Street map of the Fairhaven headquarters area"></div>
  </div>

  <div class="abs f-col" style="left:895px">
    <h4 class="f-title">About Team</h4>
    <p class="f-text">Enim congue blandit. Lorem ipsum dolor sit amet, consectetur adipiscing elit. Quisque consectetur interdum finibus. Vestibulum ante ipsum primis in faucibus orci. luctus et ultrices posuere.</p>
    <p class="f-text" style="margin-top:14px">Cubilia cras blandit finibus ipsum, id porttitor arcu volutpat a. Integer iaculis erat nec justo malesuada faucibus vel tempus sapien. Vivamus aliquam euismod tristique.</p>
  </div>

  <div class="abs f-divider"></div>
  <p class="abs copyright">Copyright 2020. All Rights Reserved by Skyward Path Labs</p>
</footer>

</body>
</html>
```